Wren Vehicle Polishing (Mobile detail)

I need a business card made up. I'd like it to be different in some form, either raised, embossed, debossed, something cool that stands out. (preferably embossed text somewhere in it). I will be including the Initial png file. Let me know if you need the photoshop of adobe illustrator file to work with.

Information to be included: Text: XXX-XXX-XXXX Phone: XXX-XXX-XXXX Email: wrenpolishcrew@mailbox-demo.net Website: www.socialpage-demo.net/wrenpolishKTR Hours of operation: Mon - Fri 7:00AM to 8:00PM Sat - 10:00AM to 8:00PM

Target Market(s)

Mobile automotive detailing

Industry/Entity Type

Automotive

Contact Information for Business Card

Make it stand out with embossed lettering, I'd also like the background to be glossy black or matte, something that represents a shiny car, black preferred

Requirements
Must have
• A glossy background, or something.
• My logo, pick one of them that best fits your design.
Should not have
• White background,
• something that does not stand out.

```html
<!DOCTYPE html>
<html lang="en">
<head>
<meta charset="utf-8">
<title>Wren Vehicle Polishing – Business Card</title>
<link rel="stylesheet" href="https://fonts.googleapis.com/css2?family=Open+Sans:wght@400;600;700&display=swap">
<style>
  :root{
    --stage:#2b2725;
    --card:#141415;
    --card-edge:#2a2a2c;
    --accent:#e8421d;
    --ink:#ececec;
    --ink-soft:#cfcfcf;
    --emboss-light:rgba(255,255,255,.28);
    --emboss-dark:rgba(0,0,0,.9);
  }
  *{box-sizing:border-box;margin:0;padding:0}
  html,body{width:1200px;height:724px;overflow:hidden;background:var(--stage)}
  body{font-family:"Open Sans",Arial,sans-serif;position:relative}
  .card{
    position:absolute;top:207px;width:540px;height:310px;overflow:hidden;
    background:radial-gradient(120% 120% at 30% 20%,var(--card-edge),var(--card) 60%);
    border-radius:6px;
    box-shadow:0 10px 28px rgba(0,0,0,.5),inset 0 1px 0 rgba(255,255,255,.12),inset 0 -1px 0 rgba(0,0,0,.6);
  }
  .card__gloss{
    position:absolute;inset:0;pointer-events:none;
    background:linear-gradient(115deg,rgba(255,255,255,0) 30%,rgba(255,255,255,.10) 42%,rgba(255,255,255,.02) 50%,rgba(255,255,255,0) 62%);
  }
  .card--front{left:40px}
  .card--back{left:620px}
  .brand{
    position:absolute;display:flex;align-items:center;gap:10px;
    color:var(--ink);font-weight:700;font-size:24px;letter-spacing:.2px;white-space:nowrap;
  }
  .brand__dot{width:18px;height:18px;border-radius:50%;background:var(--accent);flex:none}
  .card--front .brand{left:50%;top:50%;transform:translate(-50%,-50%)}
  .card--back .brand{left:50%;top:48px;transform:translateX(-50%);font-size:21px}
  .contact{position:absolute;left:0;right:0;top:100px;color:var(--ink);font-size:13px}
  .contact__row{display:flex;justify-content:center;align-items:center;gap:16px;margin-bottom:9px;white-space:nowrap}
  .contact__item{display:flex;align-items:center;gap:5px}
  .embossed{text-shadow:-1px -1px 0 var(--emboss-dark),1px 1px 0 var(--emboss-light)}
  .contact__name{color:var(--accent);font-weight:700;font-size:17px}
  .contact__sep{width:5px;height:5px;border-radius:50%;background:var(--accent)}
  .contact__role{color:var(--ink-soft)}
  .icon{width:10px;height:10px;flex:none}
  .contact__address,.contact__hours{text-align:center;color:var(--ink-soft);margin-bottom:7px}
  .contact__hours{font-size:12px}
  .contact__hours strong{color:var(--accent);font-weight:600}
</style>
</head>
<body>
  <section class="card card--front" aria-label="Card front">
    <div class="brand"><span class="brand__dot"></span>Wren Vehicle Polishing</div>
    <div class="card__gloss"></div>
  </section>

  <section class="card card--back" aria-label="Card back">
    <div class="brand"><span class="brand__dot"></span>Wren Vehicle Polishing</div>
    <div class="contact">
      <div class="contact__row embossed">
        <span class="contact__name">Add name</span>
        <span class="contact__sep"></span>
        <span class="contact__role">Manager</span>
      </div>
      <div class="contact__row embossed">
        <span class="contact__item">
          <svg class="icon" viewBox="0 0 10 10"><path d="M2 1 L4 3 L3 4 Q4 6 6 7 L7 6 L9 8 L8 9.5 Q2 8 .5 2 Z" fill="#e8421d"/></svg>
          555 014 2290
        </span>
        <span class="contact__item">
          <svg class="icon" viewBox="0 0 10 10"><rect x="2.5" y=".5" width="5" height="9" rx="1" fill="none" stroke="#e8421d" stroke-width="1.2"/></svg>
          555-014-7731
        </span>
      </div>
      <div class="contact__row embossed">
        <span class="contact__item">
          <svg class="icon" viewBox="0 0 10 10"><circle cx="5" cy="5" r="4.2" fill="none" stroke="#e8421d" stroke-width="1.2"/><path d="M1 5 H9 M5 1 Q2.5 5 5 9 M5 1 Q7.5 5 5 9" fill="none" stroke="#e8421d" stroke-width=".8"/></svg>
          www.socialpage-demo.net/wrenpolishKTR
        </span>
      </div>
      <div class="contact__row embossed">
        <span class="contact__item">
          <svg class="icon" viewBox="0 0 10 10"><text x="5" y="8.5" text-anchor="middle" font-size="10" font-weight="700" fill="#e8421d" font-family="Open Sans, sans-serif">@</text></svg>
          wrenpolishcrew@mailbox-demo.net
        </span>
      </div>
      <p class="contact__address embossed">418 Larkspur Lane Suite 7 Kestrel, IL 60000</p>
      <p class="contact__hours embossed"><strong>Mon – Fri</strong> 7:00AM to 8:00PM &nbsp;·&nbsp; <strong>Sat</strong> 10:00AM to 8:00PM</p>
    </div>
    <div class="card__gloss"></div>
  </section>
</body>
</html>
```